The book will contain the papers written by presenters at the Fresh Horizons in Beyond-Veil Dialogue conference held by the Institute for Luminous and Awareness Research. There will be something like 19 chapters, each about a different method people are using today to have afterlife communication with loved ones on the other side. The cover must be upbeat, inspiring, full of joy and life. Nothing with ghosts or cemeteries or skeletons or hauntings. It's about family members communicating with loved ones who are alive and well, just living on a different plane. Any image of uniting, love, and togetherness is a plus. The author name is Institute for Luminous and Awareness Research.

```html
<!DOCTYPE html>
<html lang="en">
<head>
<meta charset="utf-8">
<title>Fresh Horizons in Beyond-Veil Dialogue — Book Cover</title>
<link rel="stylesheet" href="https://fonts.googleapis.com/css2?family=Cinzel:wght@400;500;600&display=swap">
<style>
  :root {
    --title-cyan: #34c6f2;
    --subtitle-ink: #1d2a38;
    --imprint-white: #ffffff;
    --emblem-navy: #1f3f7a;
    --cloud-slate: #3b4a5f;
    --sky-blue: #88a7c4;
    --sun-glow: #fff4b8;
    --sun-gold: #efd36a;
    --hill-green: #79ad36;
    --forest-green: #3f7d25;
    --lake-teal: #2c8a86;
    --lake-deep: #1d7f93;
  }
  html, body {
    margin: 0;
    padding: 0;
    width: 950px;
    height: 1200px;
    overflow: hidden;
    background: #ffffff;
  }
  .cover {
    position: relative;
    width: 950px;
    height: 1200px;
    overflow: hidden;
    font-family: "Cinzel", "Times New Roman", serif;
  }
  .cover-scene {
    position: absolute;
    inset: 0;
    background:
      radial-gradient(ellipse 420px 220px at 50% 50%, rgba(255,250,210,0.95), rgba(255,240,170,0.55) 45%, rgba(255,240,170,0) 100%),
      linear-gradient(180deg,
        var(--cloud-slate) 0%,
        #556780 14%,
        var(--sky-blue) 28%,
        #d9d6a8 40%,
        var(--sun-glow) 47%,
        var(--sun-gold) 53%,
        var(--hill-green) 58%,
        var(--forest-green) 66%,
        #4f9a3c 71%,
        var(--lake-teal) 76%,
        #3fa7a8 86%,
        var(--lake-deep) 100%);
  }
  .cover-title {
    position: absolute;
    left: 66px;
    top: 150px;
    margin: 0;
    color: var(--title-cyan);
    font-weight: 400;
    font-size: 104px;
    line-height: 96px;
    letter-spacing: 4px;
  }
  .cover-title span { display: block; }
  .cover-subtitle {
    position: absolute;
    left: 80px;
    right: 80px;
    top: 528px;
    margin: 0;
    text-align: center;
    color: var(--subtitle-ink);
    font-size: 17px;
    line-height: 23px;
    letter-spacing: 1.6px;
    text-transform: uppercase;
    font-weight: 500;
  }
  .imprint {
    position: absolute;
    left: 0;
    right: 0;
    bottom: 36px;
    text-align: center;
    color: var(--imprint-white);
  }
  .imprint-mark {
    display: inline-flex;
    align-items: center;
    gap: 10px;
    margin-bottom: 10px;
    font-size: 30px;
    font-weight: 500;
    letter-spacing: 2px;
  }
  .imprint-dot {
    width: 34px;
    height: 34px;
    border-radius: 50%;
    background: var(--emblem-navy);
  }
  .imprint-name {
    margin: 0;
    font-size: 16px;
    letter-spacing: 1.5px;
    text-transform: uppercase;
    font-weight: 500;
  }
</style>
</head>
<body>
  <main class="cover">
    <div class="cover-scene" role="img" aria-label="Photograph of a bright sunrise breaking through dark clouds over green forested hills and a calm turquoise lake"></div>

    <h1 class="cover-title">
      <span>Fresh</span>
      <span>Horizons</span>
      <span>In beyond-veil</span>
      <span>Dialogue</span>
    </h1>

    <p class="cover-subtitle">19 chapters, each about a different method people are using today to have afterlife communication with loved ones on the other side</p>

    <footer class="imprint">
      <div class="imprint-mark"><span class="imprint-dot"></span>ILAR</div>
      <p class="imprint-name">Institute for Luminous and Awareness Research</p>
    </footer>
  </main>
</body>
</html>
```